" Minha empresa basicamente funciona da seguinte forma, visito os clientes, pego todas as ideias (Briefing), levo para a empresa, elaboramos o melhor projeto possivel para aquele cliente, apresentamos o projeto, o cliente aprovando, começamos a fabricação. E estamos sempre envolvidos em eventos para trazer tecnologia para nossos clientes. "

```html
<!DOCTYPE html>
<html lang="pt-BR">
<head>
<meta charset="utf-8">
<title>Marvello – Papel timbrado</title>
<link href="https://fonts.googleapis.com/css2?family=Montserrat:wght@400&family=Arimo:wght@400&display=swap" rel="stylesheet">
<style>
  :root {
    --backdrop: #d6d7d8;
    --paper: #ffffff;
    --charcoal: #3c3c3e;
    --gold: #b89c7e;
    --ink: #2b2b2b;
    --muted: #6a6a6a;
    --rule: #444446;
  }
  html, body {
    margin: 0;
    padding: 0;
    width: 1200px;
    height: 1200px;
    overflow: hidden;
    background: var(--backdrop);
  }
  .letterhead {
    position: absolute;
    left: 288px;
    top: 163px;
    width: 624px;
    height: 864px;
    background: var(--paper);
    box-shadow: 0 2px 8px rgba(0,0,0,0.12);
    font-family: "Arimo", Arial, sans-serif;
    color: var(--ink);
  }
  .brand {
    position: absolute;
    left: 20px;
    top: 22px;
    display: flex;
    align-items: center;
    gap: 10px;
  }
  .brand-square {
    width: 26px;
    height: 26px;
    background: var(--gold);
  }
  .brand-name {
    font-family: "Montserrat", Arial, sans-serif;
    font-weight: 400;
    font-size: 23px;
    letter-spacing: 1px;
    color: var(--gold);
  }
  .header-band {
    position: absolute;
    left: 0;
    top: 5px;
    width: 624px;
    height: 62px;
  }
  .header-phones {
    position: absolute;
    right: 52px;
    top: 17px;
    text-align: right;
    font-size: 10px;
    line-height: 12px;
    color: #ffffff;
  }
  .body-text {
    position: absolute;
    left: 66px;
    top: 226px;
    width: 500px;
    font-size: 10px;
    line-height: 14.4px;
    margin: 0;
  }
  .body-text p { margin: 0; }
  .terms {
    position: absolute;
    left: 66px;
    top: 522px;
    font-size: 10px;
    line-height: 14.4px;
  }
  .terms p { margin: 0; }
  .signoff {
    position: absolute;
    left: 66px;
    top: 660px;
    font-size: 10px;
  }
  .signature-line {
    position: absolute;
    left: 408px;
    top: 706px;
    width: 150px;
    height: 1px;
    background: var(--ink);
  }
  .footer-bar {
    position: absolute;
    left: 0;
    top: 798px;
    width: 624px;
    height: 9px;
    background: linear-gradient(180deg, #6f6f71 0%, var(--rule) 60%, #2f2f31 100%);
  }
  .footer-contact {
    position: absolute;
    left: 0;
    top: 822px;
    width: 624px;
    text-align: center;
    font-size: 10px;
    line-height: 14px;
    color: var(--muted);
  }
  .footer-contact p { margin: 0; }
  .footer-contact .gap { margin-left: 14px; }
</style>
</head>
<body>
  <main class="letterhead">
    <svg class="header-band" viewBox="0 0 624 62" aria-hidden="true">
      <polygon points="352,0 624,0 624,62 330,62" fill="var(--charcoal)"/>
      <polygon points="346,0 350,0 328,62 324,62" fill="var(--gold)"/>
    </svg>
    <div class="brand">
      <div class="brand-square"></div>
      <div class="brand-name">MARVELLO</div>
    </div>
    <div class="header-phones">
      <div>+00 00 0000-0000</div>
      <div>+00 00 0000-0000</div>
    </div>

    <div class="body-text">
      <p>Prezado cliente, agradecemos a confiança depositada em nosso trabalho. Após a visita técnica, reunimos todas as ideias apresentadas no briefing. Nossa equipe elaborou o melhor projeto possível para cada ambiente da sua casa. Os móveis foram pensados com atenção aos detalhes, aos materiais e ao uso diário. Apresentamos a seguir as condições gerais da proposta, os prazos previstos e as etapas de produção. Com a sua aprovação, iniciamos a fabricação em nossa fábrica, com acompanhamento técnico em todas as fases. A montagem é feita por profissionais treinados, que cuidam do ambiente e entregam tudo limpo e organizado. Participamos de feiras e eventos do setor para trazer novas tecnologias e acabamentos aos nossos clientes. Ficamos à disposição para ajustar qualquer detalhe do projeto antes do início da produção. Agradecemos a oportunidade e esperamos transformar seus ambientes com conforto, beleza e funcionalidade. Todos os itens possuem garantia e assistência técnica após a entrega. Em caso de dúvidas, entre em contato com nosso atendimento pelos canais abaixo.</p>
      <p>Cordialmente.</p>
    </div>

    <div class="terms">
      <p>Condições da proposta:</p>
      <p>Prazo de entrega de quarenta e cinco dias úteis</p>
      <p>Pagamento em até dez parcelas</p>
      <p>Validade de quinze dias</p>
      <p>Montagem inclusa</p>
    </div>

    <div class="signoff">Responsável técnico</div>
    <div class="signature-line"></div>

    <div class="footer-bar"></div>
    <div class="footer-contact">
      <p>contato@marvello.com.br<span class="gap">www.marvello.com.br</span></p>
      <p>End. Rua completa | Nº | Bairro | Cidade | CEP | UF | Brasil</p>
    </div>
  </main>
</body>
</html>
```